WordPress Website Redesign for Local, Craft Distillery

We have a WordPress site that is up and active, but it needs a full re-design. The template is slow, it doesn't look pretty, and it's not mobile device friendly.

Use your expertise to make it pretty and functional. We're about to get a lot of web traffic and we can't afford to upset potential customers!

Target Market(s)

21 to 50, both male and female

Number of Pages Required

3 page

Font styles to use
Serif
Sans Serif
Decorative
Script

Requirements
Must have
• Product Info
• Reservation system for the tasting room
• Age Verification
• Company history
• Use info from current Wordpress site: www.harborwrenspirits.com
Nice to have
• Where to buy page
• Blog

```html
<!DOCTYPE html>
<html lang="en">
<head>
<meta charset="utf-8">
<title>Harbor Wren Spirits Co.</title>
<link href="https://fonts.googleapis.com/css2?family=Lato:wght@400;700&family=Merriweather:ital,wght@0,400;0,700;1,400&display=swap" rel="stylesheet">
<style>
:root{
  --navy:#1c3a8c;
  --navy-deep:#15307a;
  --ink:#2b2b2b;
  --muted:#6b6b6b;
  --rule:#e2e2e2;
  --white:#ffffff;
  --sky:#9cc3e6;
  --sea:#3d6f9c;
  --sand:#b8a98e;
  --office:#c8cdd2;
  --dusk:#4a4f57;
}
*{margin:0;padding:0;box-sizing:border-box}
html,body{width:1200px;height:3998px;overflow:hidden}
body{font-family:"Lato",sans-serif;color:var(--ink);background:var(--white);position:relative}
.serif{font-family:"Merriweather",serif}
a{color:inherit;text-decoration:none}
.wrap{width:834px;margin:0 auto;position:relative}

/* top bar */
.topbar{height:36px;border-bottom:1px solid var(--rule);font-size:12px;color:var(--muted)}
.topbar .wrap{display:flex;align-items:center;justify-content:space-between;height:36px}
.topbar .links{display:flex;gap:26px;align-items:center;color:var(--navy)}
.dot-icon{width:10px;height:10px;border-radius:50%;background:var(--navy);display:inline-block}

/* header */
.header{height:156px;text-align:center;border-bottom:1px solid var(--rule)}
.brand{display:inline-flex;flex-direction:column;align-items:center;margin-top:12px;gap:6px}
.brand-mark{width:56px;height:56px;border-radius:50%;background:var(--navy)}
.brand-name{font-family:"Merriweather",serif;font-weight:700;font-size:13px;color:var(--navy);letter-spacing:1px;text-transform:uppercase}
.nav{display:flex;justify-content:center;gap:44px;margin-top:20px;font-size:13px;color:var(--navy);font-style:italic;font-family:"Merriweather",serif}

/* hero */
.hero{height:440px;background:linear-gradient(180deg,var(--sky) 0%,#cfe0ef 45%,var(--sea) 62%,#7f8a8f 75%,var(--sand) 100%);position:relative}
.hero-arrow{position:absolute;top:200px;width:26px;height:40px;background:rgba(0,0,0,.35)}
.hero-arrow.left{left:0}.hero-arrow.right{right:0}

/* company history */
.history{text-align:center;padding-top:30px;height:172px}
.eyebrow{font-family:"Merriweather",serif;font-style:italic;font-size:15px;color:var(--navy)}
.history h2{font-family:"Merriweather",serif;font-style:italic;font-weight:400;font-size:25px;line-height:38px;margin-top:10px;color:var(--ink)}

.about{height:234px;display:flex;gap:40px;padding-top:12px}
.about-photo{width:402px;height:205px;background:linear-gradient(135deg,#3a3d48,#8a6a4a 60%,#d7d4cc)}
.about-text{width:390px;padding-top:2px}
.about-label{font-size:12px;font-weight:700;color:var(--navy);text-transform:uppercase;letter-spacing:.5px}
.about-text h3{font-family:"Merriweather",serif;font-style:italic;font-weight:400;font-size:21px;margin:10px 0 14px}
.about-text p{font-size:12.5px;line-height:20px;color:var(--muted)}
.btn{display:inline-block;background:var(--navy);color:var(--white);font-size:12px;font-weight:700;padding:11px 24px;margin-top:18px;letter-spacing:.5px}

/* split band */
.split{height:418px;display:flex}
.split-pane{width:600px;padding:38px 0 0 0}
.split-left{background:linear-gradient(135deg,#2a2c33,#5a5e66 60%,#3b3e45);color:var(--white);padding-left:183px;padding-right:30px}
.split-right{background:var(--navy);color:var(--white);padding-left:82px;padding-right:150px}
.split h3{font-family:"Merriweather",serif;font-weight:400;font-size:24px;margin-bottom:18px}
.split .lead{font-family:"Merriweather",serif;font-size:17px;margin-bottom:20px}
.split p{font-size:13.5px;line-height:19px}
.split ul{list-style:none;font-size:12px;line-height:17px;margin:6px 0 16px}
.split-left li::before{content:"\2022";margin-right:8px}
.split-right li{margin-bottom:15px;display:flex;gap:10px}
.split-right li::before{content:"\00BB"}

/* features */
.features{height:280px;display:flex;gap:23px;padding-top:46px}
.feature{width:190px}
.feature svg{display:block;height:30px;margin-bottom:18px}
.feature h4{font-family:"Merriweather",serif;font-size:15px;font-weight:400;margin-bottom:16px}
.feature p{font-size:12px;line-height:17px;color:var(--muted);margin-bottom:20px}
.more{font-size:12px;font-weight:700;color:var(--navy)}

/* testimonial */
.testimonial{height:420px;background:linear-gradient(120deg,#d9dde1,var(--office) 40%,#7d8a96 70%,#eceef0);position:relative}
.quote-box{position:absolute;left:35px;top:115px;width:363px;height:177px;background:rgba(28,58,140,.88);color:var(--white);padding:26px 24px}
.quote-box p{font-size:14px;line-height:19px;font-weight:700}
.quote-box span{display:block;font-size:10px;margin-top:20px;letter-spacing:1px}

/* team */
.team-head{text-align:center;padding-top:52px;height:198px}
.team-head .label{font-size:12px;font-weight:700;color:var(--navy);text-transform:uppercase}
.team-head h2{font-family:"Merriweather",serif;font-weight:400;font-size:24px;line-height:36px;margin-top:18px}
.team{display:flex;gap:23px;height:419px}
.member{width:190px}
.member-photo{height:183px;background:linear-gradient(180deg,#f2f2f2,#d8dbe0 60%,#2e3440)}
.member h5{font-family:"Merriweather",serif;font-size:15px;font-weight:400;margin-top:28px}
.member .role{font-size:11px;font-weight:700;margin-top:10px;padding-bottom:12px;border-bottom:1px solid var(--rule)}
.member p{font-size:11px;line-height:16px;color:var(--muted);margin-top:12px;padding-bottom:16px;border-bottom:1px solid var(--rule)}
.member .social{display:flex;gap:14px;margin-top:14px}
.member .social i{width:9px;height:9px;border-radius:50%;background:#555;display:block}

/* quote band */
.band{height:422px;background:linear-gradient(110deg,#2b2e35,var(--dusk) 40%,#8c8e90 70%,#3a3c42);display:flex;align-items:center;justify-content:center}
.band p{font-family:"Merriweather",serif;font-size:22px;line-height:40px;color:var(--white);text-align:center;width:720px}

/* consultation */
.consult{height:461px;padding-top:68px}
.consult h2{font-family:"Merriweather",serif;font-weight:400;font-size:23px;text-align:center}
.consult .sub{font-size:13px;line-height:18px;color:var(--muted);text-align:center;margin-top:14px}
.fields{display:flex;gap:22px;margin-top:38px}
.field{flex:1;height:30px;border:1px solid var(--rule);font-size:10px;color:#aaa;padding:9px 12px}
.area{height:150px;margin-top:19px;border:1px solid var(--rule);font-size:10px;color:#aaa;padding:10px 12px}
.send{display:inline-block;background:var(--navy);color:var(--white);font-size:13px;font-weight:700;padding:10px 26px;margin-top:11px}

/* footer */
.footer{height:325px;background:linear-gradient(180deg,#8fb6d6,#5c7f9d 50%,#20252e);color:var(--white);text-align:center;padding-top:128px}
.footer h2{font-family:"Merriweather",serif;font-weight:400;font-size:21px;letter-spacing:2px;text-transform:uppercase}
.footer nav{margin-top:82px;font-size:11px;display:flex;justify-content:center;gap:14px}
.footer nav span{opacity:.6}
.footer small{display:block;font-size:10px;margin-top:36px;opacity:.85}
</style>
</head>
<body>

<div class="topbar">
  <div class="wrap">
    <span>CALL US: 123 . 465 . 789</span>
    <div class="links"><a>Contact</a><a>FAQ</a><span class="dot-icon"></span><span class="dot-icon"></span><span class="dot-icon"></span><span class="dot-icon"></span></div>
  </div>
</div>

<header class="header">
  <div class="brand"><span class="brand-mark"></span><span class="brand-name">Harbor Wren Spirits Co.</span></div>
  <nav class="nav"><a>Home</a><a>Company history</a><a>Product</a><a>Blog</a><a>Age Verification</a><a>Contact Us</a></nav>
</header>

<section class="hero" role="img" aria-label="Three bottles of spirits on a sandy shore in front of a bay and city skyline">
  <span class="hero-arrow left"></span><span class="hero-arrow right"></span>
</section>

<section class="history wrap">
  <div class="eyebrow">Company History</div>
  <h2>Lorem ipsum dolor sit amet, consectetur adipiscing elit.<br>Phasellus eget imperdiet lectus. Cras egestas interdum nibh,</h2>
</section>

<section class="about wrap">
  <div class="about-photo" role="img" aria-label="Tasting room with a flag on the wall and a framed sign above a wooden counter"></div>
  <div class="about-text">
    <div class="about-label">About the Harbor Wren Spirits</div>
    <h3>Lorem Ipsum Dolor Sid Amet</h3>
    <p>Aenean malesuada libero suscipit ultricies mollis. Morbi non massa erat. Nulla a leo tristique, mattis urna vel, luctus lacus. Nam tincidunt ligula magna, ac molestie libero eleifend ac non.</p>
    <a class="btn">LEARN MORE</a>
  </div>
</section>

<section class="split">
  <div class="split-pane split-left" role="img" aria-label="Darkened photo of people at a bar table with a positioning summary over it">
    <h3>Positioning</h3>
    <p>We are priced to be the Well Spirit in a Craft Bar or Restaurant</p>
    <ul>
      <li>At $11.33 Price to Wholesaler, Recommended Price to Retail is $16.66</li>
      <li>This is just a dollar or two more than the Mainstream Competitors</li>
      <li>Easy upsell to craft spirits from Mainstream in Craft Bars</li>
      <li>"Pour cold price your drink $5 more with a craft spirit, and make an extra $20 a bottle"</li>
      <li>We are priced below</li>
    </ul>
    <p>We are priced below our Craft Competition</p>
    <ul>
      <li>Our Recommended Price to Consumer is $24.99</li>
      <li>Direct Competitors range from $29.99 to $39.99 for Gin, Rum, and Spiced Rum</li>
    </ul>
  </div>
  <div class="split-pane split-right">
    <h3>Our Customer</h3>
    <div class="lead">Core Demographic is 21-35 Years Old</div>
    <ul>
      <li>Craft Beer Drinker- May not have ever tried Traditional American Lagers</li>
      <li>Drinks Craft Cocktails- Will spend $12 on a Whiskey Sour using a mass produced bourbon</li>
      <li>Most likely has never tried a true "Craft" spirit due to lack of options and deceptive marketing</li>
      <li>Wants Small, Local, Artisanal ingredients</li>
      <li>Our Pricing allows our customers to try craft spirits without having to break the bank</li>
    </ul>
  </div>
</section>

<section class="features wrap">
  <div class="feature">
    <svg viewBox="0 0 30 30" width="30"><polygon points="15,2 19,11 28,12 21,18 23,27 15,22 7,27 9,18 2,12 11,11" fill="none" stroke="#777" stroke-width="1.6"/></svg>
    <h4>Our Product Line</h4>
    <p>Aenean malesuada libero suscipit ultricies mollis. Morbi non massa erat. Nulla a leo tristique, mattis urna vel, luctus lacus. Nam tincidunt ligula magna</p>
    <a class="more">READ MORE</a>
  </div>
  <div class="feature">
    <svg viewBox="0 0 30 30" width="30"><circle cx="15" cy="9" r="7" fill="#777"/><path d="M3 29c0-8 5-12 12-12s12 4 12 12z" fill="#777"/></svg>
    <h4>Our Customer</h4>
    <p>Aenean malesuada libero suscipit ultricies mollis. Morbi non massa erat. Nulla a leo tristique, mattis urna vel, luctus lacus. Nam tincidunt ligula magna</p>
    <a class="more">READ MORE</a>
  </div>
  <div class="feature">
    <svg viewBox="0 0 30 30" width="30"><path d="M3 11h6l14-8v24L9 19H3z" fill="#777"/><rect x="7" y="19" width="5" height="8" fill="#777"/></svg>
    <h4>Event Marketing</h4>
    <p>Aenean malesuada libero suscipit ultricies mollis. Morbi non massa erat. Nulla a leo tristique, mattis urna vel, luctus lacus. Nam tincidunt ligula magna</p>
    <a class="more">READ MORE</a>
  </div>
  <div class="feature">
    <svg viewBox="0 0 30 30" width="30"><rect x="2" y="9" width="26" height="18" rx="2" fill="#777"/><rect x="10" y="4" width="10" height="6" fill="none" stroke="#777" stroke-width="2"/></svg>
    <h4>Our Opportunity</h4>
    <p>Aenean malesuada libero suscipit ultricies mollis. Morbi non massa erat. Nulla a leo tristique, mattis urna vel, luctus lacus. Nam tincidunt ligula magna</p>
    <a class="more">READ MORE</a>
  </div>
</section>

<section class="testimonial wrap" role="img" aria-label="Two business people shaking hands in a bright office">
  <div class="quote-box">
    <p>Lorem ipsum dolor sit amet, consectetuer adipiscing elit, sed diam nonummy nibh euismod tincidunt ut laoreet dolore magna aliquam erat volutpat dolore magna aliquam erat volutpat.</p>
    <span>JOHN SMITH</span>
  </div>
</section>

<section class="team-head wrap">
  <div class="label">Our Legal Team</div>
  <h2>Lorem ipsum dolor sit amet, consectetur adipiscing<br>elit. Duis blandit molestie ipsum eget placerat.</h2>
</section>

<section class="team wrap">
  <div class="member">
    <div class="member-photo" role="img" aria-label="Portrait of Hans Summer in a suit"></div>
    <h5>Hans Summer</h5><div class="role">CEO</div>
    <p>Lorem ipsum dolor sit amet, consectetur adipiscing elit. Duis blandit molestie ipsum placerat. Maecenas eget imperdiet quam</p>
    <div class="social"><i></i><i></i><i></i><i></i></div>
  </div>
  <div class="member">
    <div class="member-photo" role="img" aria-label="Portrait of Jack Nicholas in a suit"></div>
    <h5>Jack Nicholas</h5><div class="role">Manager</div>
    <p>Lorem ipsum dolor sit amet, consectetur adipiscing elit. Duis blandit molestie ipsum placerat. Maecenas eget imperdiet quam</p>
    <div class="social"><i></i><i></i><i></i><i></i></div>
  </div>
  <div class="member">
    <div class="member-photo" role="img" aria-label="Portrait of Martha Done in a blazer"></div>
    <h5>Martha Done</h5><div class="role">Business Lawyer</div>
    <p>Lorem ipsum dolor sit amet, consectetur adipiscing elit. Duis blandit molestie ipsum placerat. Maecenas eget imperdiet quam</p>
    <div class="social"><i></i><i></i><i></i><i></i></div>
  </div>
  <div class="member">
    <div class="member-photo" role="img" aria-label="Portrait of John Doe in a suit"></div>
    <h5>John Doe</h5><div class="role">CEO</div>
    <p>Lorem ipsum dolor sit amet, consectetur adipiscing elit. Duis blandit molestie ipsum placerat. Maecenas eget imperdiet quam</p>
    <div class="social"><i></i><i></i><i></i><i></i></div>
  </div>
</section>

<section class="band" role="img" aria-label="Business meeting with people shaking hands behind a quote">
  <p>Lorem ipsum dolor sit amet, vix erat audiam ei. Cum doctus civibus efficiantur in. Nec id tempor imperdiet deterruisset, doctus volumus explicari qui ex.</p>
</section>

<section class="consult wrap">
  <h2>Request a Free Consultation</h2>
  <p class="sub">Aenean malesuada libero suscipit ultricies<br>mollis. Morbi non massa erat. Nulla a leo tristique, mattis urna vel.</p>
  <div class="fields"><div class="field">Your Name Here</div><div class="field">Your Email Address</div><div class="field">Subject</div></div>
  <div class="area">Your Message Here</div>
  <a class="send">SEND</a>
</section>

<footer class="footer" role="img" aria-label="Faded bottles in front of a bay and city skyline">
  <h2>Harbor Wren Spirits Co.</h2>
  <nav><a>HOME</a><span>|</span><a>ABOUT</a><span>|</span><a>BLOG</a><span>|</span><a>CONTACT</a></nav>
  <small>© Copyright 2016 www.harborwrenspirits.com . All rights reserved.</small>
</footer>

</body>
</html>
```